VerdaMetrix PowerPoint Presentation Design

I am looking for a PowerPoint design for a new company based in Dallas, Texas called VerdaMetrix. We provide extremely powerful predictive and prescriptive analytics software focused on the Internet of Things (IoT) market. Our initial products are called VMX Foundry and VMX Pulse. We would like to see designs that support our logo design, which is attached.

I AM LOOKING FOR A THEME TO BE DEVELOPED FOR THE TITLE SLIDE AND INSIDE SLIDES OF A PRESENTATION. I AM NOT LOOKING FOR SOMEONE TO TAKE MY CONTENT AND CREATE A COMPLETE PRESENTATION.

Target Market(s)

Advanced Analytics, Internet of Things

Industry/Entity Type

It Company

Requirements
Must have
• Bolder colors, but they must work with the logo
Nice to have
• I prefer that the design incorporate the them of "connectivity" or "connectedness" to reflect the IoT market and "intelligence" or "smart" to reflect the analytics aspect of the business
Should not have
• I don't want people represented in the graphics scheme

```html
<!DOCTYPE html>
<html lang="en">
<head>
<meta charset="utf-8">
<title>VerdaMetrix Presentation Theme</title>
<link href="https://fonts.googleapis.com/css2?family=Roboto:ital,wght@0,300;0,400;0,500;0,700;1,700&family=Open+Sans:wght@400;600&display=swap" rel="stylesheet">
<style>
:root{
  --stage:#333333;
  --brand-blue:#1757a6;
  --bar-blue:#0d55a8;
  --brand-orange:#f5a623;
  --bar-green:#12b04b;
  --bar-gray:#c3c3c3;
  --placeholder:#d9d9d9;
  --text-dark:#444444;
  --text-muted:#8a8a8a;
  --white:#ffffff;
}
*{margin:0;padding:0;box-sizing:border-box}
html,body{width:1200px;height:1200px;overflow:hidden;background:var(--stage);font-family:"Roboto",Arial,sans-serif}
.slide{position:absolute;width:507px;height:381px;background:var(--white);overflow:hidden}
.slide-title-page{left:74px;top:20px}
.slide-about{left:601px;top:20px}
.slide-team{left:74px;top:413px}
.slide-product{left:601px;top:413px}
.slide-brand{left:74px;top:805px}
.slide-chart{left:601px;top:805px}

.abs{position:absolute}
.brand-name{display:flex;align-items:center;gap:4px;font-family:"Roboto",sans-serif;font-weight:500;color:var(--brand-blue);white-space:nowrap}
.brand-name .dot{width:.4em;height:.4em;border-radius:50%;background:var(--brand-orange)}

/* title slide */
.hero-band{left:0;top:0;width:100%;height:244px;background:var(--brand-blue)}
.hero-stripe{left:0;top:244px;width:100%;height:10px;background:var(--brand-orange)}
.hero-text{right:53px;top:146px;text-align:right;color:var(--white)}
.hero-text .welcome{font-size:22px;font-weight:700;line-height:1.1}
.hero-text .tagline{font-size:18px;font-weight:300;line-height:1.25}
.hero-text .date{font-size:10px;font-family:"Open Sans",sans-serif;margin-top:2px}
.title-brand{right:50px;top:312px;font-size:27px}
.copyright{left:34px;top:355px;font-size:5px;color:var(--text-muted)}

/* inner slides */
.header{left:0;top:0;width:100%;height:52px;background:var(--brand-blue)}
.header h2{position:absolute;left:39px;top:12px;font-size:17px;font-weight:700;color:var(--white);letter-spacing:.2px}
.header .subtitle{position:absolute;left:39px;top:33px;font-size:12px;color:var(--brand-orange)}
.header .page-no{position:absolute;right:36px;top:40px;font-size:10px;font-weight:700;color:var(--white)}
.footer{left:0;top:353px;width:100%;height:12px;display:flex;align-items:center}
.footer .rule{flex:1;height:2px;background:var(--brand-orange)}
.footer .brand-name{font-size:14px;margin:0 9px}
.footer .rule.short{flex:0 0 90px}
.intro{left:41px;top:82px;font-size:13px;color:var(--brand-blue)}

/* about */
.about-photo{left:34px;top:94px;width:179px;height:208px;background:var(--placeholder)}
.about-copy{left:236px;top:95px;width:232px;font-family:"Open Sans",sans-serif;color:var(--text-muted)}
.about-copy .lead{font-size:7px;font-weight:600;color:var(--text-dark);margin-bottom:12px}
.about-copy p{font-size:6.4px;line-height:15.2px;text-align:justify}

/* team */
.member{top:127px;width:80px;text-align:center}
.member .portrait{width:80px;height:95px;background:var(--placeholder);border-top-right-radius:11px}
.member .name{margin-top:10px;font-size:9px;font-weight:500;color:var(--brand-orange)}
.member .role{margin-top:8px;font-size:6px;font-weight:700;font-style:italic;color:var(--text-dark)}
.member .bio{margin-top:6px;font-size:5px;line-height:6px;color:var(--text-muted)}

/* product */
.screen{width:128px;height:142px;border-radius:3px;background:linear-gradient(180deg,#2b2b2b 0 68%,#d6d6d6 68% 78%,#ededed 78%)}
.product-name{font-size:11px;font-weight:700;color:#222}
.product-desc{font-family:"Open Sans",sans-serif;font-size:6px;line-height:8.3px;color:var(--text-muted)}

/* brand slide */
.texture{left:0;top:0;width:100%;height:100%;background:radial-gradient(ellipse at center,#f7f7f7 0%,#ebebeb 70%,#e2e2e2 100%)}
.brand-centre{left:0;top:0;width:100%;height:100%;display:flex;justify-content:center;align-items:center}
.brand-centre .brand-name{font-size:34px}

/* chart */
.chart{left:0;top:0}
.chart-note{left:40px;top:283px;width:430px;font-family:"Open Sans",sans-serif;font-size:6.4px;line-height:12.8px;color:var(--text-muted)}
</style>
</head>
<body>

<section class="slide slide-title-page">
  <div class="abs hero-band"></div>
  <div class="abs hero-stripe"></div>
  <div class="abs hero-text">
    <div class="welcome">WELCOME</div>
    <div class="tagline">TO OUR PRESENTATION</div>
    <div class="date">January 2016</div>
  </div>
  <div class="abs brand-name title-brand">VerdaMetrix<span class="dot"></span></div>
  <div class="abs copyright">© 2015 VerdaMetrix inc. All Rights Reserved.</div>
</section>

<section class="slide slide-about">
  <header class="abs header"><h2>ABOUT US</h2><div class="subtitle">Sub Title text &nbsp;goes here</div><div class="page-no">1</div></header>
  <div class="abs about-photo" role="img" aria-label="Photo placeholder"></div>
  <div class="abs about-copy">
    <div class="lead">Lorem ipsum dolor sit amet, <i>consectetur adipiscing elit.</i></div>
    <p>Praesent sodales odio sit amet odio tristique quis tempus odio Lorem ipsum dolor sit amet, consectetur adipiscing elit. Lorem ipsum dolor sit amet, consectetur adipiscing elit. Praesent sodales odio sit amet odio tristique quis tempus odio Lorem ipsum dolor sit amet, consectetur adipiscing elit. Lorem ipsum dolor sit amet, consectetur adipiscing elit. Lorem ipsum dolor sit amet, <b><i>consectetur adipiscing elit.</i></b> Praesent sodales odio sit amet odio tristique quis tempus odio Lorem ipsum dolor sit amet, consectetur adipiscing elit. Lorem ipsum dolor sit amet, consectetur adipiscing elit. Praesent sodales odio sit amet odio tristique quis tempus odio Lorem ipsum dolor adipiscing elit. Lorem ipsum dolor sit amet, consectetur adipiscing elit.</p>
  </div>
  <div class="abs footer"><span class="rule"></span><span class="brand-name">VerdaMetrix<span class="dot"></span></span><span class="rule short"></span></div>
</section>

<section class="slide slide-team">
  <header class="abs header"><h2>OUR TEAM</h2><div class="subtitle">Sub Title text &nbsp;goes here</div><div class="page-no">2</div></header>
  <div class="abs intro">Lorem ipsum dolor sit amet consectetur</div>
  <div class="abs member" style="left:39px"><div class="portrait" role="img" aria-label="Team member photo placeholder"></div><div class="name">JHON DOE</div><div class="role">Manager</div><div class="bio">Lorem ipsum dolor sit amet, consectetur Praesent sodales odio sit amet odio tristique quis tempus odio</div></div>
  <div class="abs member" style="left:154px"><div class="portrait" role="img" aria-label="Team member photo placeholder"></div><div class="name">JHON DOE</div><div class="role">Manager</div><div class="bio">Lorem ipsum dolor sit amet, consectetur Praesent sodales odio sit amet odio tristique quis tempus odio</div></div>
  <div class="abs member" style="left:269px"><div class="portrait" role="img" aria-label="Team member photo placeholder"></div><div class="name">JHON DOE</div><div class="role">Manager</div><div class="bio">Lorem ipsum dolor sit amet, consectetur Praesent sodales odio sit amet odio tristique quis tempus odio</div></div>
  <div class="abs member" style="left:384px"><div class="portrait" role="img" aria-label="Team member photo placeholder"></div><div class="name">JHON DOE</div><div class="role">Manager</div><div class="bio">Lorem ipsum dolor sit amet, consectetur Praesent sodales odio sit amet odio tristique quis tempus odio</div></div>
  <div class="abs footer"><span class="rule"></span><span class="brand-name">VerdaMetrix<span class="dot"></span></span><span class="rule short"></span></div>
</section>

<section class="slide slide-product">
  <header class="abs header"><h2>OUR PRODUCT</h2><div class="subtitle">Sub Title text &nbsp;goes here</div><div class="page-no">3</div></header>
  <div class="abs intro" style="left:39px;top:75px">Lorem ipsum dolor sit amet consectetur</div>
  <div class="abs screen" style="left:40px;top:114px" role="img" aria-label="Desktop monitor showing the VMX Foundry product screen"></div>
  <div class="abs product-name" style="right:53px;top:118px">VMX Pulse</div>
  <div class="abs product-desc" style="right:52px;top:137px;width:205px;text-align:right">Terra Bond Polymeric sand is fast-setting, so you save precious time. You can use it for both drainage and non-drainage base systes. Ideal for commercial and residential applications. Available in Black Diamond, Beige, Grey and Ivory colours.</div>
  <div class="abs screen" style="left:333px;top:187px" role="img" aria-label="Desktop monitor showing the VMX Pulse product screen"></div>
  <div class="abs product-name" style="left:45px;top:280px">VMX Foundry</div>
  <div class="abs product-desc" style="left:45px;top:296px;width:205px;text-align:justify">Terra Bond Polymeric sand is fast-setting, so you save precious time. You can use it for both drainage and non-drainage base systes. Ideal for commercial and residential applications. Available in Black Diamond, Beige, Grey and Ivory colours.</div>
  <div class="abs footer"><span class="rule"></span><span class="brand-name">VerdaMetrix<span class="dot"></span></span><span class="rule short"></span></div>
</section>

<section class="slide slide-brand">
  <div class="abs texture" role="img" aria-label="Soft grey paper texture background"></div>
  <div class="abs brand-centre"><span class="brand-name">VerdaMetrix<span class="dot"></span></span></div>
</section>

<section class="slide slide-chart">
  <header class="abs header"><h2>GRAPHIC CHART SLIDE</h2><div class="subtitle">Sub Title text &nbsp;goes here</div><div class="page-no">5</div></header>
  <div class="abs intro" style="left:42px;top:77px">Lorem ipsum dolor sit amet consectetur</div>
  <svg class="abs chart" width="507" height="381" viewBox="0 0 507 381" font-family="Open Sans, sans-serif">
    <g stroke="#ececec" stroke-width="0.6">
      <line x1="44" y1="111" x2="440" y2="111"/><line x1="44" y1="132" x2="440" y2="132"/>
      <line x1="44" y1="153" x2="440" y2="153"/><line x1="44" y1="174" x2="440" y2="174"/>
      <line x1="44" y1="195" x2="440" y2="195"/><line x1="44" y1="216" x2="440" y2="216"/>
      <line x1="44" y1="237" x2="440" y2="237"/>
    </g>
    <line x1="44" y1="258" x2="440" y2="258" stroke="#999" stroke-width="0.8"/>
    <g font-size="4.5" fill="#888" text-anchor="end">
      <text x="40" y="113">70</text><text x="40" y="134">60</text><text x="40" y="155">50</text>
      <text x="40" y="176">40</text><text x="40" y="197">30</text><text x="40" y="218">20</text>
      <text x="40" y="239">10</text><text x="40" y="260">0</text>
    </g>
    <g>
      <rect x="56" y="190.3" width="14" height="67.7" fill="var(--bar-green)"/>
      <rect x="70" y="205.1" width="14" height="52.9" fill="var(--bar-gray)"/>
      <rect x="84" y="226.3" width="14" height="31.7" fill="var(--bar-blue)"/>
      <rect x="98" y="232.6" width="14" height="25.4" fill="var(--brand-orange)"/>

      <rect x="134" y="190.3" width="14" height="67.7" fill="var(--bar-green)"/>
      <rect x="148" y="184" width="14" height="74" fill="var(--bar-gray)"/>
      <rect x="162" y="209.4" width="14" height="48.6" fill="var(--bar-blue)"/>
      <rect x="176" y="232.6" width="14" height="25.4" fill="var(--brand-orange)"/>

      <rect x="213" y="198.8" width="14" height="59.2" fill="var(--bar-green)"/>
      <rect x="227" y="215.7" width="14" height="42.3" fill="var(--bar-gray)"/>
      <rect x="241" y="131.2" width="14" height="126.8" fill="var(--bar-blue)"/>
      <rect x="255" y="232.6" width="14" height="25.4" fill="var(--brand-orange)"/>

      <rect x="291" y="232.6" width="14" height="25.4" fill="var(--bar-green)"/>
      <rect x="305" y="194.6" width="14" height="63.4" fill="var(--bar-gray)"/>
      <rect x="319" y="156.5" width="14" height="101.5" fill="var(--bar-blue)"/>
      <rect x="333" y="213.6" width="14" height="44.4" fill="var(--brand-orange)"/>

      <rect x="370" y="226.3" width="14" height="31.7" fill="var(--bar-green)"/>
      <rect x="384" y="203" width="14" height="55" fill="var(--bar-gray)"/>
      <rect x="398" y="148.1" width="14" height="109.9" fill="var(--bar-blue)"/>
      <rect x="412" y="198.8" width="14" height="59.2" fill="var(--brand-orange)"/>
    </g>
    <g font-size="4.5" fill="#888" text-anchor="middle">
      <text x="85" y="267">5/1/2015</text><text x="163" y="267">6/1/2015</text>
      <text x="242" y="267">7/1/2015</text><text x="320" y="267">8/1/2015</text>
      <text x="399" y="267">9/1/2015</text>
    </g>
    <g font-size="4.5" fill="#888">
      <rect x="449" y="174" width="7" height="5" fill="var(--bar-blue)"/><text x="460" y="178.5">Indonesia</text>
      <rect x="449" y="191" width="7" height="5" fill="var(--bar-green)"/><text x="460" y="195.5">Indonesia</text>
      <rect x="449" y="208" width="7" height="5" fill="var(--brand-orange)"/><text x="460" y="212.5">Indonesia</text>
      <rect x="449" y="225" width="7" height="5" fill="var(--bar-gray)"/><text x="460" y="229.5">Indonesia</text>
    </g>
  </svg>
  <p class="abs chart-note">Lorem ipsum dolor sit amet, <b><i>consectetur adipiscing elit.</i></b> Praesent sodales odio sit amet odio tristique quis tempus odio Lorem ipsum dolor sit amet, consectetur adipiscing elit. Lorem ipsum dolor sit amet, consectetur adipiscing elit. Praesent sodales odio sit amet odio tristique quis tempus odio Lorem ipsum dolor sit amet, consectetur adipiscing elit. Lorem ipsum dolor sit amet, consectetur adipiscing elit.</p>
  <div class="abs footer"><span class="rule"></span><span class="brand-name">VerdaMetrix<span class="dot"></span></span><span class="rule short"></span></div>
</section>

</body>
</html>
```